Zielgruppe
Wir sind KT Helio Werkstatt GmbH mit Sitz in Basel Schweiz. Wir bieten die volle Palette von Elektronikdienstleistungen. Besonders aber Photovoltaik (Solar) auf Einfamilienhäusern und Gewerbeeinheiten, Smart Home Automation mit Quarvid (Partner) und allgemeine Elektrikerdienstleistungen in Häusern und Wohnung.
USP
• Regionale Firma, BS, BL,AG
○ Daher schnelle Reaktion im Störungsfall. Garantierte Entstörung
• Umsetzung innert 2-3 Monate
• Planung und Durchführung aus einer Hand.
• Umsetzung auch in der PV Installation nur durch eigene Mitarbeiter
• Tellvia Förderung, bis zu 6TCHF
• Kompetent, freundlich
• Eidgenössich diplomierter Elektroinstallateur (Meister)
• EFZ (Eidgenösisch Fährigkeitszeugnis)
• 1 Jahr Existenz
• Quarvid goldpartner
• Nur Doppelglasmodule mit 25 Jahre Garantie, 10 Jahre auf Wechselrichter und Batterie
• Planung mittels CAD/*D Planung, technische Tool
• Genaues und schnelles Angebot innert 5 Werktagen
USP:
• Stromkosten sparen
• Autark werden, unabhängig von Strompreisentwicklung
• Umwelt schützen
WUNSCHKUNDE
• Soziodemografisch
○ Eigentümer
○ Gehobene Mittelklasse
• Lokalität in Basel und Umgebung
Aufgabenstellung
Medien unter: https://cloudbox.dremantu.ch/index.php/s/xLqTe8RwZnM4vHY
Logo ist dort vorhanden.
Hintergrund hell (weiss, hellgrau bspw.)
Schriftart
Verlinkungen zu Social Media:
• Facebook
• Linkedin
• Instagram
Beispielseiten, die gefallen:
Grenz Licht Werk (grenz-licht-werk.ch) Prio
Counter mit

```html
<!DOCTYPE html>
<html lang="de">
<head>
<meta charset="utf-8">
<title>KT Helio Werkstatt GmbH – Kostenloses Angebot</title>
<link href="https://fonts.googleapis.com/css2?family=Baloo+2:wght@700;800&family=Hind:wght@400;500&family=Montserrat:wght@500;600;700&display=swap" rel="stylesheet">
<style>
:root{
  --green:#007a1e;
  --green-btn:#1f8a2e;
  --red:#e42126;
  --slate:#7d8c9c;
  --text:#2c2c2c;
  --footer:#333333;
  --track:#e2e2e2;
}
*{margin:0;padding:0;box-sizing:border-box}
html,body{width:1200px;height:2265px;overflow:hidden;background:#fff}
body{position:relative;font-family:'Hind',sans-serif;color:var(--text)}
.topbar{position:absolute;left:0;top:0;width:1200px;height:60px;background:var(--green);display:flex;justify-content:center;align-items:center;gap:42px;color:#fff;font-family:'Montserrat',sans-serif;font-weight:600;font-size:21px}
.topbar .item{display:flex;align-items:center;gap:16px}
.topbar .ico{width:34px;height:34px;border-radius:50%;background:#fff;display:flex;align-items:center;justify-content:center}
.hero{position:absolute;left:0;top:60px;width:1200px;height:605px}
.hero-photo{position:absolute;inset:0;background:linear-gradient(100deg,#eef0f2 0%,#e3e6ea 40%,#c9cdd2 62%,#b9aea2 75%,#8f9aa6 100%)}
.hero-fade{position:absolute;inset:0;background:linear-gradient(90deg,rgba(255,255,255,.55) 0%,rgba(255,255,255,.25) 60%,rgba(255,255,255,0) 100%)}
.brand{position:absolute;left:105px;top:34px;display:flex;align-items:center;gap:10px;font-family:'Montserrat',sans-serif;font-weight:600;font-size:22px;color:var(--green);line-height:1.15;width:230px}
.brand .mark{width:34px;height:34px;background:var(--green);flex:none}
.nav{position:absolute;left:457px;top:60px;display:flex;gap:18px;font-family:'Montserrat',sans-serif;font-weight:500;font-size:21px;color:#3b3b3b}
.btn-contact{position:absolute;left:980px;top:53px;width:124px;height:45px;background:var(--red);color:#fff;font-family:'Montserrat',sans-serif;font-weight:600;font-size:21px;display:flex;align-items:center;justify-content:center;border-radius:3px;box-shadow:0 2px 4px rgba(0,0,0,.2)}
.hero h1{position:absolute;left:105px;top:188px;font-family:'Baloo 2',sans-serif;font-weight:800;font-size:63px;line-height:68px;color:var(--slate);letter-spacing:-.5px;white-space:nowrap}
.hero p{position:absolute;left:105px;top:344px;width:650px;font-size:20.5px;line-height:27.2px;color:#2a2a2a}
.progress{position:absolute;left:137px;top:767px;display:flex;align-items:center;gap:24px;font-size:15px}
.progress .track{width:863px;height:5px;background:var(--track);border-radius:3px;position:relative}
.progress .fill{position:absolute;left:0;top:0;height:5px;width:173px;background:var(--green);border-radius:3px}
.question{position:absolute;left:0;top:854px;width:1200px;text-align:center;font-family:'Baloo 2',sans-serif;font-weight:800;font-size:51px;line-height:51px;color:var(--slate)}
.option{position:absolute;left:410px;display:flex;align-items:center;gap:32px}
.option .illus{width:102px;height:102px;border-radius:8px}
.option label{display:flex;align-items:center;gap:10px;font-size:20.5px;color:#5a6672}
.radio{width:17px;height:17px;border:1.5px solid #555;border-radius:50%;display:inline-flex;align-items:center;justify-content:center}
.radio.on{border-color:var(--green)}
.radio.on::after{content:"";width:9px;height:9px;border-radius:50%;background:var(--green)}
.btn-next{position:absolute;left:551px;top:1422px;width:110px;height:45px;background:var(--green-btn);color:#fff;font-family:'Montserrat',sans-serif;font-weight:600;font-size:21px;display:flex;align-items:center;justify-content:center;border-radius:3px;box-shadow:0 2px 4px rgba(0,0,0,.2)}
.green-fade{position:absolute;left:0;top:1485px;width:1200px;height:314px;background:linear-gradient(180deg,#fff 0%,#c9e3cc 45%,#79bd83 75%,var(--green) 100%)}
.footer{position:absolute;left:0;top:1799px;width:1200px;height:466px;background:var(--footer);color:#fff;font-family:'Montserrat',sans-serif}
.f-company{position:absolute;left:98px;top:52px;width:300px}
.f-company h3{font-weight:700;font-size:23px;line-height:26px;margin-bottom:22px}
.f-company p{font-weight:700;font-size:16.5px;line-height:26px}
.f-company a{color:#fff;text-decoration:underline}
.f-col{position:absolute;top:64px;width:240px;text-align:center;font-weight:500;font-size:19px;line-height:25.7px}
.f-col h4{font-weight:700;font-size:19.5px;margin-bottom:10px}
.social{position:absolute;left:525px;top:2072px;display:flex;gap:30px}
.social span{width:29px;height:29px;border-radius:50%;background:var(--green);display:block}
.badge{position:absolute;left:472px;top:2139px;width:255px;height:45px;background:linear-gradient(90deg,#c9a45c 0%,#c9a45c 82%,#1a1a1a 82%)}
</style>
</head>
<body>
<header class="topbar">
  <div class="item"><span class="ico"><svg width="18" height="18" viewBox="0 0 24 24"><path fill="#007a1e" d="M6.6 10.8c1.4 2.8 3.8 5.1 6.6 6.6l2.2-2.2c.3-.3.7-.4 1-.2 1.1.4 2.3.6 3.6.6.6 0 1 .4 1 1V20c0 .6-.4 1-1 1C10.6 21 3 13.4 3 4c0-.6.4-1 1-1h3.5c.6 0 1 .4 1 1 0 1.3.2 2.5.6 3.6.1.3 0 .7-.2 1z"/></svg></span>+49 170 555 18 24</div>
  <div class="item"><span class="ico"><svg width="18" height="14" viewBox="0 0 20 14"><rect x="1" y="1" width="18" height="12" rx="2" fill="none" stroke="#007a1e" stroke-width="2"/><path d="M2 2l8 6 8-6" fill="none" stroke="#007a1e" stroke-width="2"/></svg></span>info@kthelio-werkstatt.de</div>
</header>

<section class="hero">
  <div class="hero-photo" role="img" aria-label="Foto: Handwerker mit Helm vor Solarmodulen, unscharf im Hintergrund"></div>
  <div class="hero-fade"></div>
  <div class="brand"><span class="mark"></span><span>KT Helio Werkstatt GmbH</span></div>
  <nav class="nav"><span>Über uns</span><span>Dienstleistungen</span><span>Referenzen</span><span>Jobs</span></nav>
  <a class="btn-contact">Kontakt</a>
  <h1>Sichern Sie sich Ihr<br>kostenloses Angebot!</h1>
  <p>Erschließen Sie die unbegrenzte Kraft der Sonne für Ihr Zuhause oder Ihr Unternehmen! Jetzt ist der perfekte Zeitpunkt, den Schritt in Richtung nachhaltige Energie zu wagen. Fordern Sie noch heute Ihr kostenfreies, unverbindliches Angebot an und entdecken Sie, wie unsere maßgeschneiderten Photovoltaiklösungen Ihre Energieeffizienz revolutionieren können. Klicken Sie unten, um Ihren Weg zu einer grüneren Zukunft zu beginnen.</p>
</section>

<div class="progress"><span>20%</span><div class="track"><div class="fill"></div></div></div>

<h2 class="question">Wie möchten Sie Ihren selbst<br>erzeugten Strom nutzen?</h2>

<div class="option" style="top:1003px">
  <div class="illus" role="img" aria-label="Illustration: Solarmodule mit Sonne" style="background:linear-gradient(160deg,#fbeec4,#e4e7e0 60%,#cfe6c9)"></div>
  <label><span class="radio on"></span>Eigenverbrauch ohne Speicher</label>
</div>
<div class="option" style="top:1139px">
  <div class="illus" role="img" aria-label="Illustration: Solarmodul mit Batteriespeicher" style="background:linear-gradient(160deg,#fbeec4,#d6e0ef 55%,#b9cdf0)"></div>
  <label><span class="radio"></span>Eigenverbrauch mit Speicher</label>
</div>
<div class="option" style="top:1275px">
  <div class="illus" role="img" aria-label="Illustration: bunte Fragezeichen" style="background:linear-gradient(120deg,#fbe6a6,#c3d6f2 50%,#bfe8dc)"></div>
  <label><span class="radio"></span>Noch nicht entschieden</label>
</div>

<a class="btn-next">Weiter</a>

<div class="green-fade"></div>

<footer class="footer">
  <div class="f-company">
    <h3>KT Helio Werkstatt GmbH</h3>
    <p>Am Lindenhof 12<br>D-79540 Lörrach-Haagen<br>Telefon: +49 170 555 18 24<br>E-Mail: <a>info@kthelio-werkstatt.de</a></p>
  </div>
  <div class="f-col" style="left:356px"><h4>Navigation</h4>Über uns<br>Referenzen<br>Jobs<br>Kontakt</div>
  <div class="f-col" style="left:618px"><h4>Dienstleistungen</h4>Elektroinstallation<br>E-Mobility<br>Photovoltaik<br>Smart-Home mit<br>Quarvid</div>
  <div class="f-col" style="left:879px"><h4>Rechtliches</h4>Impressum<br>Datenschutzerklärung<br>Widerrufsbelehrung<br>AGB</div>
</footer>
<div class="social" aria-label="Social-Media-Links"><span aria-label="Soziales Netzwerk 1"></span><span aria-label="Soziales Netzwerk 2"></span><span aria-label="Soziales Netzwerk 3"></span></div>
<div class="badge" role="img" aria-label="Partner-Auszeichnung"></div>
</body>
</html>
```